Emergency Response Company Needs a Web Design

To go along with a completed logo redesign, we are looking to update and modernize the design and feel of our site.The emergency response planning we do is based around the oil and gas industry. Our existing site at http://www.quorvanteplan.com/ will give some insight in to what we do. For more related insight, here are some direct competitors:
http://www.lumeridgecare.ca/index.php
http://www.tessorwindplan.com/
http://pollixfuels.com/
http://dravonltd.ca/company.php
http://www.keel-aidworks.com/

Industry/Entity Type

Oil And Gas

```html
<!DOCTYPE html>
<html lang="en">
<head>
<meta charset="utf-8">
<title>Quorvante Resource Consultants</title>
<link href="https://fonts.googleapis.com/css2?family=Open+Sans:wght@300;400;600&display=swap" rel="stylesheet">
<style>
:root{
  --bg-top:#b9cbd6;
  --bg-bottom:#eef2f4;
  --page:#ffffff;
  --text:#333333;
  --muted:#555555;
  --link:#1a9bd7;
  --rule:#e6e6e6;
  --pink:#d6537f;
  --pink-dark:#b8365f;
  --yellow:#fcb800;
  --orange:#f15022;
  --logo-red:#c4262e;
}
*{margin:0;padding:0;box-sizing:border-box}
html,body{width:852px;height:1200px;overflow:hidden}
body{font-family:'Open Sans',Arial,sans-serif;color:var(--text);
  background:linear-gradient(180deg,var(--bg-top) 0,var(--bg-bottom) 260px,var(--bg-bottom) 100%);position:relative}
.page{position:absolute;left:19px;top:6px;width:812px;height:1194px;background:var(--page);box-shadow:0 0 4px rgba(0,0,0,.15)}
.abs{position:absolute}
a{color:var(--link);text-decoration:none}

/* header */
.header{position:absolute;left:0;top:0;width:812px;height:81px;border-bottom:1px solid #eee}
.brand{position:absolute;left:52px;top:33px;display:flex;align-items:center;gap:6px}
.brand-name{font-size:22px;font-weight:400;color:#222;letter-spacing:.5px;line-height:1}
.brand-sub{font-size:6.5px;color:#222;letter-spacing:.3px;display:block;margin-top:2px}
.brand-mark{width:14px;height:14px;background:var(--logo-red);border-radius:50%}
.nav{position:absolute;top:35px;left:306px;display:flex;font-size:10px;color:#444}
.nav span{padding:0 16px;border-left:1px solid #ddd;line-height:11px}
.nav span:first-child{border-left:none;padding-left:0}
.contact{position:absolute;left:707px;top:35px;font-size:10px;color:#444}

/* slider */
.slider{position:absolute;left:39px;top:84px;width:734px;height:253px}
.slider-shadow{position:absolute;left:10px;top:250px;width:724px;height:12px;background:linear-gradient(180deg,rgba(0,0,0,.35),rgba(0,0,0,0));}
.slide-photo{position:absolute;left:0;top:0;width:254px;height:253px;background:linear-gradient(135deg,#6b7a72,#2e3333 60%,#c86a2a)}
.slide-panel{position:absolute;left:254px;top:0;width:480px;height:253px;background:radial-gradient(ellipse at 50% 45%,#e06a92,var(--pink) 55%,var(--pink-dark))}
.slide-rule{position:absolute;left:34px;top:80px;width:2px;height:79px;background:#fff}
.slide-title{position:absolute;left:67px;top:76px;font-size:26px;font-weight:300;line-height:28px;color:#fff}
.slide-arrows{position:absolute;left:520px;top:232px}

/* services */
.h2{position:absolute;font-size:20px;font-weight:400;color:#333}
.service{position:absolute;top:416px;width:166px}
.service h3{font-size:11.5px;font-weight:400;color:#333;height:30px}
.service .thumb{width:166px;height:82px}
.service p{font-size:8px;line-height:11.5px;color:#444;margin-top:21px}
.service .more{display:block;text-align:right;font-size:8px;margin-top:15px}
.service .more.active span{background:var(--link);color:#fff;padding:1px 3px}

/* tabs */
.tabs{position:absolute;left:35px;top:680px;width:506px;height:246px;border:1px solid #e2e2e2;border-top:none}
.tab-row{position:absolute;left:0;top:0;width:506px;height:25px;display:flex;background:#f3f3f3;border-top:1px solid #e2e2e2;border-bottom:1px solid #e2e2e2}
.tab{flex:1;font-size:8px;text-align:center;line-height:24px;color:#333;border-left:1px solid #e2e2e2}
.tab.active{flex:0 0 127px;background:#fff;border-left:none;border-bottom:1px solid #fff;margin-top:-8px;height:33px;border-top:1px solid #e2e2e2;line-height:26px;font-size:9px}
.tab-title{position:absolute;left:24px;top:60px;font-size:14px;font-weight:400}
.tab-text{position:absolute;left:24px;top:86px;width:330px;font-size:8px;line-height:11.5px;color:#444}
.tab-list{position:absolute;left:24px;top:121px;width:330px;list-style:none}
.tab-list li{font-size:8px;height:25.5px;line-height:25px;border-bottom:1px solid #eee}
.tab-list li:last-child{border-bottom:none}
.tab-list li::before{content:"→ ";color:#666;font-size:7px}
.tab-photo{position:absolute;left:379px;top:74px;width:102px;height:152px;background:linear-gradient(160deg,#8a8f7d,#e0662a 55%,#2b2e2c)}

/* promo */
.promo{position:absolute;left:580px;width:190px;height:116px;color:#fff}
.promo.yellow{top:680px;background:var(--yellow)}
.promo.orange{top:810px;background:var(--orange)}
.promo-title{position:absolute;left:12px;bottom:22px;font-size:19px;font-weight:300;line-height:18px}
.promo svg{position:absolute;right:19px;top:16px}

/* footer */
.rule{position:absolute;left:18px;width:760px;height:1px;background:var(--rule)}
.fcol{position:absolute;top:998px}
.fcol h4{font-size:9.5px;font-weight:400;color:#333;margin-bottom:13px}
.fcol a{display:block;font-size:8px;line-height:16.5px}
.socials{position:absolute;left:34px;top:1163px;display:flex;gap:5px}
.socials span{width:10px;height:10px;background:#5a6f8f}
.legal{position:absolute;right:41px;top:1164px;font-size:7.5px;color:#333}
.legal span{padding:0 5px;border-left:1px solid #ccc}
.legal span:first-child{border-left:none}
</style>
</head>
<body>
<div class="page">
  <header class="header">
    <div class="brand">
      <div>
        <span class="brand-name">QUORVANTE</span>
        <span class="brand-sub">RESOURCE CONSULTANTS LTD</span>
      </div>
      <span class="brand-mark"></span>
    </div>
    <nav class="nav">
      <span>Home</span><span>Shortcodes</span><span>Layouts</span><span>Portfolio</span><span>Blog</span>
    </nav>
    <div class="contact">Get in touch &nbsp;<span style="color:#aaa">›</span></div>
  </header>

  <section class="slider">
    <div class="slider-shadow"></div>
    <div class="slide-photo" role="img" aria-label="Emergency crew in orange safety vests attending an injured person"></div>
    <div class="slide-panel">
      <div class="slide-rule"></div>
      <h1 class="slide-title">The Preferred Supplier of<br>Emergency Response<br>Management Services</h1>
      <svg class="slide-arrows" width="50" height="14" viewBox="0 0 50 14">
        <polyline points="8,2 3,7 8,12" fill="none" stroke="#fff" stroke-width="2"/>
        <line x1="25" y1="3" x2="25" y2="11" stroke="rgba(255,255,255,.5)" stroke-width="1"/>
        <polyline points="42,2 47,7 42,12" fill="none" stroke="#fff" stroke-width="2"/>
      </svg>
    </div>
  </section>

  <h2 class="h2" style="left:38px;top:370px">Welcome to Quorvante</h2>

  <article class="service" style="left:37px">
    <h3>Emergency Response Plans</h3>
    <div class="thumb" role="img" aria-label="Responders in hazmat suits beside a rail tank car" style="background:linear-gradient(180deg,#9fb7cf,#b9b9b4 55%,#7a7a6a)"></div>
    <p>Lorem ipsum dolor sit amet, consectetur adipiscing elit. Nullam consectetur est quis mauris accumsan eleifend</p>
    <a class="more" href="#">Read More</a>
  </article>
  <article class="service" style="left:228px">
    <h3>Public &nbsp;Consultation</h3>
    <div class="thumb" role="img" aria-label="Audience seated at a public meeting" style="background:linear-gradient(180deg,#c9b7a0,#6e5a48 60%,#3a2e26)"></div>
    <p>Lorem ipsum dolor sit amet, consectetur adipiscing elit. Nullam consectetur est quis mauris accumsan eleifend</p>
    <a class="more active" href="#"><span>Read More</span></a>
  </article>
  <article class="service" style="left:418px">
    <h3>GIS Mapping</h3>
    <div class="thumb" role="img" aria-label="Aerial view of a residential street layout" style="background:linear-gradient(135deg,#6f7f5a,#8c9a78 50%,#5d6b4c)"></div>
    <p>Lorem ipsum dolor sit amet, consectetur adipiscing elit. Nullam consectetur est quis mauris accumsan eleifend</p>
    <a class="more" href="#">Read More</a>
  </article>
  <article class="service" style="left:608px">
    <h3>Training</h3>
    <div class="thumb" role="img" aria-label="Trainer presenting at a flip chart to colleagues" style="background:linear-gradient(90deg,#d8dadc,#f1f1f1 55%,#9a9a9a)"></div>
    <p>Lorem ipsum dolor sit amet, consectetur adipiscing elit. Nullam consectetur est quis mauris accumsan eleifend</p>
    <a class="more" href="#">Read More</a>
  </article>

  <h2 class="h2" style="left:32px;top:630px">Features &amp; downloads</h2>

  <section class="tabs">
    <div class="tab-row">
      <div class="tab active">Why Choose us?</div>
      <div class="tab">Developing</div>
      <div class="tab">Our profile</div>
      <div class="tab">Partnership</div>
    </div>
    <h3 class="tab-title">Let’s cooperate!</h3>
    <p class="tab-text">Lorem ipsum dolor sit amet, consectetur adipiscing elit. Nullam consectetur est quis mauris accumsan eleifend</p>
    <ul class="tab-list">
      <li><a href="#">Lorem ipsum dolor sit amet, consectetur adipiscing elit</a></li>
      <li><a href="#">Nullam consectetur est quis mauris</a></li>
      <li><a href="#">Vivamus vitae purus eros, nec ullamcorper risus</a></li>
      <li><a href="#">Curabitur auctor imperdiet mauris a suscipit</a></li>
    </ul>
    <div class="tab-photo" role="img" aria-label="Field worker in a safety vest reading documents"></div>
  </section>

  <a class="promo yellow" href="#">
    <svg width="26" height="26" viewBox="0 0 26 26"><circle cx="13" cy="13" r="11.5" fill="none" stroke="#fff" stroke-width="2"/><path d="M7 13h11M14 9l4 4-4 4" fill="none" stroke="#fff" stroke-width="2"/></svg>
    <span class="promo-title">Premium Partners<br>Program</span>
  </a>
  <a class="promo orange" href="#">
    <svg width="26" height="26" viewBox="0 0 26 26"><circle cx="13" cy="13" r="11.5" fill="none" stroke="#fff" stroke-width="2"/><path d="M7 13h11M14 9l4 4-4 4" fill="none" stroke="#fff" stroke-width="2"/></svg>
    <span class="promo-title">Try our Online<br>Consulting</span>
  </a>

  <div class="rule" style="top:964px"></div>

  <div class="fcol" style="left:34px">
    <h4>Socials</h4>
    <a href="#">Friendwall</a><a href="#">Snapfolio</a><a href="#">Chirpline</a><a href="#">Reelhub</a><a href="#">Circlespace</a>
  </div>
  <div class="fcol" style="left:225px">
    <h4>Popular resources</h4>
    <a href="#">How to Write a Blog</a><a href="#">Create a Blog in 4 Steps</a><a href="#">15 Tips to Increase Traffic</a><a href="#">20 Blog Post Ideas</a><a href="#">Top 10 for Beginner Bloggers</a>
  </div>
  <div class="fcol" style="left:416px">
    <h4>Blogroll</h4>
    <a href="#">Blogs Blog</a><a href="#">Roll Up Roll Up</a><a href="#">Blog Free</a><a href="#">Pressleaf Blog</a><a href="#">Start Blogging</a>
  </div>
  <div class="fcol" style="left:605px">
    <h4>About</h4>
    <a href="#">Marrowby</a><a href="#">Careers</a><a href="#">Company news</a><a href="#">Investor relations</a><a href="#">Site map</a>
  </div>

  <div class="rule" style="top:1142px"></div>

  <div class="socials"><span></span><span></span><span></span><span></span><span></span></div>
  <div class="legal"><span>Contact us</span><span>Privacy statement</span><span>© 2012 Quorvante</span></div>
</div>
</body>
</html>
```